TRADESHOW BOOTH DESIGN

We Need A Trade-show Booth Design With A Tent, 2 Roll Up Signs, A Table Skirt & Backdrop We Could Use For Filming / Photo Ops. I'll give some examples of designs we like. We are a concealed Weapons Training Company Called Harbor Ridge Defense & Also Have An Academy Called The Falcon Institute. There Are Two Logos. On The Top Of The Tent Maybe You Can Alternate Logos On The Panels. The Backdrop Could Also Incorporate Both Logos.

ROLL UP BANNER 1:
The first roll up would be a welcome sign welcoming students to our class. It would display a pleasant looking person in a black golf shirt with our Harbor Ridge Defense logo in red on their right chest and a smile on their face. It would say "WELCOME TO HARBOR RIDGE DEFENSE! THANK YOU FOR TRUSTING US WITH YOUR TRAINING! IT'S AN HONOR!" It would also say: "WE WANT TO GET YOU SIGNED IN AND SEATED AS FAST AS POSSIBLE! PLEASE HAVE THE FOLLOWING INFORMATION READY:
1. YOUR PHOTO ID
2. YOUR TICKET OR RECEIPT OF PURCHASE IF YOU DON'T HAVE YOUR TICKET SO WE CAN LOOK YOU UP!
The banner would also have our logo and the following information:
- #1 Rated Firearms Training Company In America!
- Don't Settle For A Gun Shop Style Class!
- It's Not A Class, It's An Experience!

ROLL UP BANNER 2:
The other roll up banner is a mock up of a target we use in our training. I'll attach our rough design. We are trying to enhance the design of the target roll up sign so please do you just simply copy it identically. We want to refine it! All of the information is correct but it's just not on the level we want. PLEASE READ CAREFULLY: The scale on banner for the target is 77 inches tall and 33 inches wide. the silhouette on the target is 23 inches tall by 15.5 inches wide. The A and B Boxes are supposed to be located below. the silhouette target not next to it. They are 9 inches by 9 inches square. The shapes are supposed to be spread out on the left and right sides equally spaced apart with the bottom oval on the right and the hexagon on the left. at the bottom of the silhouette's torso and the blue diamond on the left and the yellow pentagon on the right of the head of the silhouette. Please follow the picture the I gave you in the brief to keep the dimensions and everything the same. I just want an artist to make the shapes and silhouette look more polished, not move them around and change the dimensions.

TABLE SKIRT:
This would incorporate our logo and would be full color on a black background. It would also say: "It's Not A Class...It's An Experience!" It will be 16' Feet long.

TENT:
This would be printed on black also and the logos would alternate between our attached Harbor Ridge Defense logo and The Falcon Institute logo. The four sides of the square tent would be as follows:
SIDE ONE: Upper roof panel would be the Harbor Ridge Defense logo and the lower flat side area would have our website written in Ethnocentric Font exactly like this: www.HarborRidgeDefense.biz with Larger letters beginning each of the first word. This helps people to see the actual words in our website better.
SIDE TWO: Upper roof panel would have The Falcon Institute Logo and the following website: www.EnrollFalconInstitute.com also in ethnocentric font and with larger letters as the first letter in each word.

BACKDROP:
This would be a backdrop for filming and taking pictures. Perhaps repeating and alternating Falcon Institute then Harbor Ridge Defense logos. Totally open to whatever ideas you may have!

Industry/Entity Type

Self Defense

Colors
ec1f27

Requirements
Must have
• Clean modern design that matches the look of the powerpoint I provided.
Nice to have
• incredible design quality
Should not have
• very good design quality

```html
<!DOCTYPE html>
<html lang="en">
<head>
<meta charset="utf-8">
<title>Harbor Ridge Defense – Training Target Roll Up</title>
<link href="https://fonts.googleapis.com/css2?family=Russo+One&family=Montserrat:wght@700;800;900&display=swap" rel="stylesheet">
<style>
  :root {
    --brand-red: #ec1f27;
    --ink: #0b0b0c;
    --panel-dark: #1c1d20;
    --panel-mid: #2a2b2f;
    --white: #ffffff;
    --box-grey: #a3a3a3;
    --rule: #3a3a3e;
    --shape-cyan: #35b6d4;
    --shape-yellow: #f6d733;
    --shape-green: #7cc22a;
    --shape-red: #e4431c;
    --shape-purple: #8a5bb8;
    --shape-orange: #f5a10d;
  }
  * { box-sizing: border-box; margin: 0; padding: 0; }
  html, body { width: 1200px; height: 2723px; overflow: hidden; background: var(--ink); }
  .banner {
    position: relative; width: 1200px; height: 2723px; overflow: hidden;
    background: var(--ink);
    font-family: "Montserrat", Arial, sans-serif; color: var(--white);
  }
  .corner-glow {
    position: absolute; width: 520px; height: 620px;
    background: radial-gradient(ellipse at center, rgba(236,31,39,.55) 0%, rgba(150,10,18,.25) 45%, rgba(0,0,0,0) 72%);
  }
  .corner-glow.top-left { left: -260px; top: -240px; }
  .corner-glow.top-right { right: -260px; top: -240px; }
  .corner-glow.bottom-left { left: -260px; bottom: -360px; }
  .corner-glow.bottom-right { right: -260px; bottom: -360px; }

  .brand-header { position: absolute; left: 0; top: 0; width: 1200px; height: 586px; text-align: center; }
  .brand-mark { position: absolute; left: 0; right: 0; top: 160px; display: flex; flex-direction: column; align-items: center; gap: 26px; }
  .brand-dot { width: 70px; height: 70px; border-radius: 50%; background: var(--brand-red); }
  .brand-name { font-family: "Russo One", Arial, sans-serif; font-size: 50px; letter-spacing: 3px; color: var(--white); }
  .headline { position: absolute; left: 0; right: 0; top: 412px; font-family: "Russo One", Arial, sans-serif; line-height: 1; }
  .headline .small { display: block; font-size: 58px; letter-spacing: 6px; color: var(--white); }
  .headline .large { display: block; margin-top: 6px; font-size: 110px; letter-spacing: 2px; color: var(--brand-red); }

  .red-rule { position: absolute; left: 0; width: 1200px; height: 8px; background: linear-gradient(90deg, rgba(236,31,39,0), var(--brand-red) 20%, var(--brand-red) 80%, rgba(236,31,39,0)); }

  .target-panel {
    position: absolute; left: 0; top: 594px; width: 1200px; height: 1297px;
    background: linear-gradient(180deg, var(--panel-mid) 0%, var(--panel-dark) 100%);
  }
  .target-art { position: absolute; left: 0; top: 594px; width: 1200px; height: 1297px; }
  .shape-number { font-family: "Montserrat", Arial, sans-serif; font-weight: 900; font-size: 84px; fill: #111; }
  .box-letter { font-family: "Montserrat", Arial, sans-serif; font-weight: 900; font-size: 230px; fill: #111; }

  .keys { position: absolute; left: 0; top: 1899px; width: 1200px; height: 650px; }
  .keys-title { position: absolute; left: 0; right: 0; top: 30px; text-align: center; font-family: "Russo One", Arial, sans-serif; line-height: 1.05; }
  .keys-title .line-one { display: block; font-size: 50px; letter-spacing: 2px; color: var(--white); }
  .keys-title .line-two { display: block; font-size: 50px; letter-spacing: 2px; color: var(--brand-red); font-style: italic; }
  .key-list { position: absolute; left: 130px; top: 178px; width: 960px; display: grid; grid-template-columns: 1fr 1fr; column-gap: 40px; }
  .key-item { display: flex; align-items: center; gap: 24px; height: 112px; border-bottom: 2px solid var(--rule); }
  .key-item:nth-last-child(-n+2) { border-bottom: none; }
  .key-icon { flex: 0 0 96px; height: 64px; display: flex; align-items: center; justify-content: center; }
  .key-icon .placeholder { width: 70px; height: 46px; border-radius: 8px; background: var(--brand-red); }
  .key-text { font-weight: 800; font-size: 26px; line-height: 1.15; text-transform: uppercase; color: var(--white); }

  .site-bar {
    position: absolute; left: 0; top: 2552px; width: 1200px; height: 74px;
    background: #151517; border-top: 4px solid var(--brand-red); border-bottom: 4px solid var(--brand-red);
    display: flex; align-items: center; justify-content: center;
    font-family: "Russo One", Arial, sans-serif; font-size: 40px; letter-spacing: 2px; color: var(--white);
  }
</style>
</head>
<body>
<main class="banner">
  <div class="corner-glow top-left" role="img" aria-label="Red halftone dot texture"></div>
  <div class="corner-glow top-right" role="img" aria-label="Red halftone dot texture"></div>
  <div class="corner-glow bottom-left" role="img" aria-label="Red halftone dot texture"></div>
  <div class="corner-glow bottom-right" role="img" aria-label="Red halftone dot texture"></div>

  <header class="brand-header">
    <div class="brand-mark">
      <span class="brand-dot"></span>
      <span class="brand-name">HARBOR RIDGE DEFENSE</span>
    </div>
    <h1 class="headline">
      <span class="small">PREPARED</span>
      <span class="large">TO PREVAIL</span>
    </h1>
  </header>

  <div class="red-rule" style="top:584px"></div>

  <section class="target-panel" role="img" aria-label="Dark carbon fibre texture"></section>

  <svg class="target-art" viewBox="0 594 1200 1297" aria-label="Training target">
    <defs>
      <radialGradient id="silhouetteFill" cx="50%" cy="40%" r="65%">
        <stop offset="0%" stop-color="#e6e6e6"/>
        <stop offset="55%" stop-color="#8a8a8a"/>
        <stop offset="100%" stop-color="#4a4a4a"/>
      </radialGradient>
      <radialGradient id="centerGlow" cx="50%" cy="50%" r="55%">
        <stop offset="70%" stop-color="#ffffff"/>
        <stop offset="100%" stop-color="#ffffff" stop-opacity="0"/>
      </radialGradient>
    </defs>

    <path class="silhouette" d="M500 650 H702 V832 H826 L872 878 V1275 L810 1350 V1395 L872 1458 H328 L390 1395 V1350 L328 1275 V878 L374 832 H500 Z"
          fill="url(#silhouetteFill)" stroke="#ffffff" stroke-width="4"/>
    <polygon points="561,698 647,698 604,750" fill="#ffffff"/>
    <rect x="462" y="889" width="268" height="256" fill="url(#centerGlow)"/>
    <rect x="482" y="909" width="228" height="216" fill="#ffffff"/>

    <polygon points="172,709 270,807 172,905 74,807" fill="var(--shape-cyan)" stroke="#fff" stroke-width="4"/>
    <text class="shape-number" x="172" y="836" text-anchor="middle">1</text>

    <polygon points="1031,714 1118,778 1085,880 977,880 944,778" fill="var(--shape-yellow)" stroke="#fff" stroke-width="4"/>
    <text class="shape-number" x="1031" y="834" text-anchor="middle">2</text>

    <circle cx="172" cy="1034" r="78" fill="var(--shape-green)" stroke="#fff" stroke-width="4"/>
    <text class="shape-number" x="172" y="1063" text-anchor="middle">3</text>

    <polygon points="999,961 1063,961 1109,1007 1109,1071 1063,1117 999,1117 953,1071 953,1007" fill="var(--shape-red)" stroke="#fff" stroke-width="4"/>
    <text class="shape-number" x="1031" y="1068" text-anchor="middle">4</text>

    <polygon points="128,1230 216,1230 260,1306 216,1382 128,1382 84,1306" fill="var(--shape-purple)" stroke="#fff" stroke-width="4"/>
    <text class="shape-number" x="172" y="1335" text-anchor="middle">5</text>

    <ellipse cx="1031" cy="1306" rx="76" ry="92" fill="var(--shape-orange)" stroke="#fff" stroke-width="4"/>
    <text class="shape-number" x="1031" y="1335" text-anchor="middle">6</text>

    <rect x="159" y="1520" width="321" height="313" fill="var(--box-grey)" stroke="#fff" stroke-width="4"/>
    <text class="box-letter" x="320" y="1760" text-anchor="middle">L</text>
    <rect x="712" y="1520" width="316" height="313" fill="var(--box-grey)" stroke="#fff" stroke-width="4"/>
    <text class="box-letter" x="870" y="1760" text-anchor="middle">R</text>
  </svg>

  <div class="red-rule" style="top:1891px"></div>

  <section class="keys">
    <h2 class="keys-title">
      <span class="line-one">FALCON INSTITUTE KEYS</span>
      <span class="line-two">TO DIFENSIVE SHOOTING</span>
    </h2>
    <ul class="key-list" style="list-style:none">
      <li class="key-item"><span class="key-icon"><span class="placeholder" role="img" aria-label="Pointing hand icon"></span></span><span class="key-text">Finger off<br>trigger</span></li>
      <li class="key-item"><span class="key-icon"><span class="placeholder" role="img" aria-label="Handgun icon"></span></span><span class="key-text">Maintain muzzle<br>awareness</span></li>
      <li class="key-item"><span class="key-icon">
        <svg width="80" height="50" viewBox="0 0 80 50" aria-label="Eye icon"><path d="M4 25 Q40 -6 76 25 Q40 56 4 25 Z" fill="none" stroke="var(--brand-red)" stroke-width="5"/><circle cx="40" cy="25" r="10" fill="var(--brand-red)"/></svg>
      </span><span class="key-text">Both eyes open</span></li>
      <li class="key-item"><span class="key-icon"><span class="placeholder" role="img" aria-label="Shooter in athletic stance icon"></span></span><span class="key-text">Athletic shooting<br>stance</span></li>
      <li class="key-item"><span class="key-icon">
        <svg width="72" height="72" viewBox="0 0 72 72" aria-label="Four-way arrows icon" fill="var(--brand-red)" stroke="var(--brand-red)" stroke-width="3">
          <line x1="36" y1="8" x2="36" y2="64"/><line x1="8" y1="36" x2="64" y2="36"/>
          <polygon points="36,2 28,14 44,14"/><polygon points="36,70 28,58 44,58"/><polygon points="2,36 14,28 14,44"/><polygon points="70,36 58,28 58,44"/>
        </svg>
      </span><span class="key-text">Minimum required<br>movement</span></li>
      <li class="key-item"><span class="key-icon"><span class="placeholder" role="img" aria-label="Front sight on target icon"></span></span><span class="key-text">Front sight focus</span></li>
      <li class="key-item"><span class="key-icon"><span class="placeholder" role="img" aria-label="Ready position icon"></span></span><span class="key-text">Maintain ready<br>position</span></li>
      <li class="key-item"><span class="key-icon"><span class="placeholder" role="img" aria-label="Balance scale icon"></span></span><span class="key-text">Balance accuracy<br>&amp; speed</span></li>
    </ul>
  </section>

  <footer class="site-bar">www.myfalcon.institute</footer>
</main>
</body>
</html>
```